LINGERIE WEBSHOP - Velora casa

We are looking for design and layout design for our webshop. We are company that sells lingerie and other connected textile products liki payamas and etc..
Our website will have approx 500 different products within 2 main catogories Woman/Man) and approx. 10 subcategories
Here is what we expect form design:
-Color pallete should be black and white (if you wish you can add some accent color)
-we want to leave feeling to customers of good quality products towards to luxury
-UX should be simple. Feel free to suggest layout
-frontpage layout, product list layout, product description layout, blog layout
-responsive design, compatible with smartphone

Target Market(s)

woman buying for themself, man buying for woman

Industry/Entity Type

Lingerie

Logo Text

VELORA CASA

Number of Pages Required

4 page

Font styles to use
Sans Serif
Decorative

Requirements
Must have
• simple UX
Nice to have
• difference for sexy/luxury lingerie and daily/cozy lingerie
Should not have
• cheap feel, unreliable

```html
<!DOCTYPE html>
<html lang="en">
<head>
<meta charset="utf-8">
<title>Velora casa — Shop</title>
<link rel="stylesheet" href="https://fonts.googleapis.com/css2?family=Josefin+Sans:wght@300&family=Playfair+Display:wght@700&family=Roboto:wght@400&family=Ubuntu:wght@300;400;500&display=swap">
<style>
:root{
  --ink:#111111;
  --paper:#ffffff;
  --footer:#161616;
  --muted:#e9e9e9;
  --dress-light:#f6ece0;
  --dress-warm:#e7a866;
}
*{box-sizing:border-box;margin:0;padding:0}
html,body{width:1200px;height:1022px;overflow:hidden;background:var(--paper);color:var(--ink)}
.page{position:relative;width:1200px;height:1022px}

.brand{position:absolute;left:88px;top:58px;font-family:"Josefin Sans",sans-serif;font-weight:300;font-size:28px;letter-spacing:0.5px;color:var(--ink)}
.main-nav{position:absolute;left:389px;top:54px;display:flex;gap:32px}
.main-nav a{font-family:"Playfair Display",serif;font-weight:700;font-size:25px;color:var(--ink);text-decoration:none}
.tools{position:absolute;top:60px;left:878px;display:flex;align-items:center}
.tools svg{display:block}

.filters{position:absolute;left:88px;top:163px;width:215px;list-style:none}
.filters li{position:relative;height:29px;border:1.5px solid var(--ink);margin-bottom:9.2px;font-family:Roboto,sans-serif;font-size:11px;line-height:26px;padding-left:11px}
.filters .toggle{position:absolute;right:6px;top:6px}
.filters li.active .toggle{right:0;top:0;width:27px;height:27px;background:var(--ink);display:flex;align-items:center;justify-content:center}

.product{position:absolute;width:196px;border:1.5px solid var(--ink);background:var(--paper);overflow:hidden}
.product.top{top:136px;height:285px}
.product.bottom{top:487px;height:160px;border-bottom:none}
.product .photo{position:absolute;left:54px;top:32px;width:86px;height:184px;border-radius:30px 30px 6px 6px;background:linear-gradient(180deg,var(--dress-light) 0%,#f1d3b1 55%,var(--dress-warm) 100%)}
.product .bar{position:absolute;left:0;right:0;bottom:0;height:38px;background:var(--footer);display:flex;align-items:center;padding:0 14px 0 17px}
.price{font-family:Roboto,sans-serif;font-size:12px;color:var(--paper);text-decoration:underline;flex:1}
.bar-icons{display:flex;gap:11px;align-items:center}

.site-footer{position:absolute;left:0;top:675px;width:1200px;height:347px;background:var(--footer);color:var(--paper);font-family:Ubuntu,sans-serif}
.to-top{position:absolute;left:126px;top:65px;display:flex;align-items:center;gap:9px;font-weight:500;font-size:16px}
.col{position:absolute;top:110px}
.col h3{font-weight:500;font-size:16px;margin-bottom:14px}
.col a{display:block;font-weight:300;font-size:16px;line-height:27.3px;color:var(--paper);text-decoration:none}
.newsletter{position:absolute;left:714px;top:101px;width:350px}
.newsletter h2{font-weight:500;font-size:28px;padding-bottom:5px;border-bottom:1.5px solid var(--paper);white-space:nowrap}
.email{display:flex;justify-content:space-between;align-items:center;height:38px;border-bottom:1.5px solid var(--paper);padding:0 6px 0 12px;font-weight:300;font-size:16px}
.legal-note{position:absolute;left:720px;top:223px;font-size:10px;line-height:14.5px;font-weight:400}
</style>
</head>
<body>
<div class="page">
  <header>
    <div class="brand">VELORA CASA</div>
    <nav class="main-nav"><a href="#">Shop</a><a href="#">Blog</a></nav>
    <div class="tools">
      <svg width="24" height="24" viewBox="0 0 24 24" fill="none" stroke="#111" stroke-width="2"><circle cx="10" cy="10" r="8"/><line x1="16" y1="16" x2="21" y2="21"/></svg>
      <svg style="margin-left:10px" width="22" height="22" viewBox="0 0 22 22" fill="none" stroke="#111" stroke-width="1.6"><line x1="2" y1="5" x2="20" y2="5"/><line x1="2" y1="11" x2="20" y2="11"/><line x1="2" y1="17" x2="20" y2="17"/><line x1="13" y1="2" x2="13" y2="8"/><line x1="8" y1="8" x2="8" y2="14"/><line x1="13" y1="14" x2="13" y2="20"/></svg>
      <svg style="margin-left:27px" width="24" height="24" viewBox="0 0 24 24" fill="none" stroke="#111" stroke-width="2"><path d="M1 3h4l3 12h12l2-9H7"/><circle cx="9" cy="20" r="1.4" fill="#111"/><circle cx="19" cy="20" r="1.4" fill="#111"/></svg>
      <svg style="margin-left:27px" width="22" height="22" viewBox="0 0 24 24" fill="none" stroke="#111" stroke-width="1.8"><path d="M12 21s-9-5.5-9-12a5 5 0 0 1 9-3 5 5 0 0 1 9 3c0 6.5-9 12-9 12z"/></svg>
      <svg style="margin-left:24px" width="18" height="18" viewBox="0 0 18 18" stroke="#111" stroke-width="1.6"><line x1="1" y1="5" x2="17" y2="5"/><line x1="1" y1="9" x2="17" y2="9"/><line x1="1" y1="13" x2="17" y2="13"/></svg>
    </div>
  </header>

  <ul class="filters">
    <li>Categories<svg class="toggle" width="15" height="15" stroke="#111" stroke-width="1.6"><line x1="7.5" y1="0" x2="7.5" y2="15"/><line x1="0" y1="7.5" x2="15" y2="7.5"/></svg></li>
    <li>Man<svg class="toggle" width="15" height="15" stroke="#111" stroke-width="1.6"><line x1="7.5" y1="0" x2="7.5" y2="15"/><line x1="0" y1="7.5" x2="15" y2="7.5"/></svg></li>
    <li class="active">woman<span class="toggle"><svg width="12" height="12" stroke="#fff" stroke-width="1.8"><line x1="1" y1="1" x2="11" y2="11"/><line x1="11" y1="1" x2="1" y2="11"/></svg></span></li>
    <li>Linger<svg class="toggle" width="15" height="15" stroke="#111" stroke-width="1.6"><line x1="7.5" y1="0" x2="7.5" y2="15"/><line x1="0" y1="7.5" x2="15" y2="7.5"/></svg></li>
    <li>Assecories<svg class="toggle" width="15" height="15" stroke="#111" stroke-width="1.6"><line x1="7.5" y1="0" x2="7.5" y2="15"/><line x1="0" y1="7.5" x2="15" y2="7.5"/></svg></li>
    <li>Shoes<svg class="toggle" width="15" height="15" stroke="#111" stroke-width="1.6"><line x1="7.5" y1="0" x2="7.5" y2="15"/><line x1="0" y1="7.5" x2="15" y2="7.5"/></svg></li>
    <li>Others<svg class="toggle" width="15" height="15" stroke="#111" stroke-width="1.6"><line x1="7.5" y1="0" x2="7.5" y2="15"/><line x1="0" y1="7.5" x2="15" y2="7.5"/></svg></li>
  </ul>

  <main>
    <article class="product top" style="left:389px"><div class="photo" role="img" aria-label="Sleeveless cream dress with orange check pattern"></div><div class="bar"><span class="price">3,325$</span><span class="bar-icons"><svg width="14" height="14" stroke="#fff" stroke-width="1.2" fill="none"><line x1="0" y1="3" x2="14" y2="3"/><line x1="0" y1="7" x2="14" y2="7"/><line x1="0" y1="11" x2="14" y2="11"/><line x1="9" y1="1" x2="9" y2="5"/><line x1="5" y1="5" x2="5" y2="9"/><line x1="9" y1="9" x2="9" y2="13"/></svg><svg width="14" height="14" viewBox="0 0 24 24" fill="none" stroke="#fff" stroke-width="2"><path d="M1 3h4l3 12h12l2-9H7"/><circle cx="9" cy="20" r="1.4"/><circle cx="19" cy="20" r="1.4"/></svg><svg width="15" height="14" viewBox="0 0 24 22" fill="none" stroke="#fff" stroke-width="2"><path d="M12 20s-9-5.5-9-12a5 5 0 0 1 9-3 5 5 0 0 1 9 3c0 6.5-9 12-9 12z"/></svg></span></div></article>
    <article class="product top" style="left:651px"><div class="photo" role="img" aria-label="Sleeveless cream dress with orange check pattern"></div><div class="bar"><span class="price">3,325$</span><span class="bar-icons"><svg width="14" height="14" stroke="#fff" stroke-width="1.2" fill="none"><line x1="0" y1="3" x2="14" y2="3"/><line x1="0" y1="7" x2="14" y2="7"/><line x1="0" y1="11" x2="14" y2="11"/><line x1="9" y1="1" x2="9" y2="5"/><line x1="5" y1="5" x2="5" y2="9"/><line x1="9" y1="9" x2="9" y2="13"/></svg><svg width="14" height="14" viewBox="0 0 24 24" fill="none" stroke="#fff" stroke-width="2"><path d="M1 3h4l3 12h12l2-9H7"/><circle cx="9" cy="20" r="1.4"/><circle cx="19" cy="20" r="1.4"/></svg><svg width="15" height="14" viewBox="0 0 24 22" fill="none" stroke="#fff" stroke-width="2"><path d="M12 20s-9-5.5-9-12a5 5 0 0 1 9-3 5 5 0 0 1 9 3c0 6.5-9 12-9 12z"/></svg></span></div></article>
    <article class="product top" style="left:912px"><div class="photo" role="img" aria-label="Sleeveless cream dress with orange check pattern"></div><div class="bar"><span class="price">3,325$</span><span class="bar-icons"><svg width="14" height="14" stroke="#fff" stroke-width="1.2" fill="none"><line x1="0" y1="3" x2="14" y2="3"/><line x1="0" y1="7" x2="14" y2="7"/><line x1="0" y1="11" x2="14" y2="11"/><line x1="9" y1="1" x2="9" y2="5"/><line x1="5" y1="5" x2="5" y2="9"/><line x1="9" y1="9" x2="9" y2="13"/></svg><svg width="14" height="14" viewBox="0 0 24 24" fill="none" stroke="#fff" stroke-width="2"><path d="M1 3h4l3 12h12l2-9H7"/><circle cx="9" cy="20" r="1.4"/><circle cx="19" cy="20" r="1.4"/></svg><svg width="15" height="14" viewBox="0 0 24 22" fill="none" stroke="#fff" stroke-width="2"><path d="M12 20s-9-5.5-9-12a5 5 0 0 1 9-3 5 5 0 0 1 9 3c0 6.5-9 12-9 12z"/></svg></span></div></article>

    <article class="product bottom" style="left:389px"><div class="photo" role="img" aria-label="Sleeveless cream dress with orange check pattern"></div></article>
    <article class="product bottom" style="left:651px"><div class="photo" role="img" aria-label="Sleeveless cream dress with orange check pattern"></div></article>
    <article class="product bottom" style="left:912px"><div class="photo" role="img" aria-label="Sleeveless cream dress with orange check pattern"></div></article>
  </main>

  <footer class="site-footer">
    <div class="to-top"><svg width="21" height="21" viewBox="0 0 22 22" fill="none" stroke="#fff" stroke-width="1.6"><circle cx="11" cy="11" r="10"/><path d="M11 16V6M7 10l4-4 4 4"/></svg>Go to top</div>
    <div class="col" style="left:127px"><h3>Site map:</h3><a href="#">Home</a><a href="#">Shop</a><a href="#">Blog</a><a href="#">About</a></div>
    <div class="col" style="left:299px"><h3>Legal</h3><a href="#">Notice</a><a href="#">Cookie policy</a><a href="#">Terms &amp; sale</a><a href="#">Accessibility</a></div>
    <div class="col" style="left:494px"><h3>Customer</h3><a href="#">Contact us</a><a href="#">FAQ</a><a href="#">Track your order</a><a href="#">Returns</a></div>
    <div class="newsletter">
      <h2>Subscribe to our newsletter</h2>
      <div class="email"><span>Your email</span><svg width="20" height="20" viewBox="0 0 22 22" fill="none" stroke="#fff" stroke-width="1.5"><circle cx="11" cy="11" r="10"/><path d="M6 11h10M12 7l4 4-4 4"/></svg></div>
    </div>
    <p class="legal-note">© Velora casa - 2007 to 2020<br>Data privacy by California state laws</p>
  </footer>
</div>
</body>
</html>
```